Lowmoor Guild - Crossroads CD Cover

To prepare a CD Cover for the single "Crossroads" by Lowmoor Guild.
You can hear the single here:
http://lowmoorguild.com/listen/

The LMG logo and backdrop are also provided if you want to incorporate them into the CD cover design, though that isn't mandatory.

Song is about deciding on taking on a serious relationship, and leaving the single life behind.

Target Market(s)

Music listeners, 18-50 yrs old, into retro 80s, Marigolds/Dune Riders

Industry/Entity Type

Music Download

Requirements
Must have
• LMG logo
• Crossroads title
Nice to have
• Use of backdrop, or facimile
Should not have
• Too obvious on the term Crossroads

```html
<!DOCTYPE html>
<html lang="en">
<head>
<meta charset="utf-8">
<title>Lowmoor Guild – Crossroads</title>
<link rel="stylesheet" href="https://fonts.googleapis.com/css2?family=Big+Shoulders+Display:wght@300&family=Lexend:wght@700&display=swap">
<style>
  :root {
    --deep-red: #5e0c06;
    --crimson: #a3180c;
    --ember: #d2360f;
    --amber: #e98a1c;
    --gold: #f3c53a;
    --coat-brown: #7a3a1c;
    --coat-cream: #d9b58a;
    --logo-yellow: #e8d84a;
    --panel: rgba(5, 3, 3, 0.86);
    --title-black: #0a0806;
  }
  html, body {
    margin: 0;
    padding: 0;
    width: 1200px;
    height: 1200px;
    overflow: hidden;
    background: #000;
  }
  .cover {
    position: relative;
    width: 1200px;
    height: 1200px;
    overflow: hidden;
  }
  .autumn-scene {
    position: absolute;
    inset: 0;
    background:
      radial-gradient(ellipse 420px 260px at 760px 870px, rgba(243, 197, 58, 0.75), transparent 70%),
      radial-gradient(ellipse 300px 300px at 150px 820px, rgba(226, 150, 40, 0.55), transparent 70%),
      radial-gradient(ellipse 700px 240px at 600px 1120px, rgba(246, 170, 40, 0.8), transparent 75%),
      linear-gradient(180deg, var(--crimson) 0%, var(--deep-red) 22%, var(--ember) 48%, var(--amber) 72%, #e4661a 88%, var(--gold) 100%);
  }
  .couple-area {
    position: absolute;
    left: 190px;
    top: 420px;
    width: 330px;
    height: 680px;
    background:
      radial-gradient(ellipse 90px 260px at 120px 300px, rgba(217, 181, 138, 0.55), transparent 75%),
      radial-gradient(ellipse 130px 330px at 210px 330px, rgba(122, 58, 28, 0.75), transparent 75%),
      radial-gradient(ellipse 110px 220px at 170px 560px, rgba(30, 16, 10, 0.55), transparent 75%);
  }
  .logo-panel {
    position: absolute;
    left: 323px;
    top: 88px;
    width: 565px;
    height: 564px;
    background: var(--panel);
  }
  .logo-panel svg,
  .title svg {
    display: block;
  }
  .band-name {
    font-family: "Big Shoulders Display", "Antonio", sans-serif;
    font-weight: 300;
    fill: var(--logo-yellow);
  }
  .title {
    position: absolute;
    left: 498px;
    top: 990px;
    width: 660px;
    height: 110px;
    margin: 0;
  }
  .title-text {
    font-family: "Lexend", "Questrial", sans-serif;
    font-weight: 700;
    fill: var(--title-black);
  }
</style>
</head>
<body>
  <main class="cover">
    <div class="autumn-scene" role="img" aria-label="Photograph of a park under red and golden autumn trees"></div>
    <div class="couple-area" role="img" aria-label="Photograph of a couple in coats embracing on the park path"></div>

    <div class="logo-panel">
      <svg width="565" height="564" viewBox="0 0 565 564" aria-label="Lowmoor Guild">
        <text class="band-name" x="287" y="252" text-anchor="middle" font-size="290" textLength="305" lengthAdjust="spacingAndGlyphs">LOWMOOR</text>
        <text class="band-name" x="287" y="507" text-anchor="middle" font-size="300" textLength="305" lengthAdjust="spacingAndGlyphs">GUILD</text>
      </svg>
    </div>

    <h1 class="title">
      <svg width="660" height="110" viewBox="0 0 660 110">
        <text class="title-text" x="0" y="100" font-size="134" textLength="652" lengthAdjust="spacingAndGlyphs">CROSSROADS</text>
      </svg>
    </h1>
  </main>
</body>
</html>
```